Chiropractic Auto Accident Billboard

Billboard for Auto Accident Chiropractor
Kestrelwood Rehab
(770) 48-SPINE
Habla Espanol
Same Day Appointments - Locations across Georgia
INJURED IN A CAR ACCIDENT?

Target Market(s)

People in Auto Accidents

Industry/Entity Type

Personal Injury

Requirements
Must have
• BIG PHONE Number

```html
<!DOCTYPE html>
<html lang="en">
<head>
<meta charset="utf-8">
<title>Kestrelwood Rehab – Auto Injury Billboard</title>
<link rel="stylesheet" href="https://fonts.googleapis.com/css2?family=Figtree:wght@400;500;800;900&display=swap">
<style>
  :root {
    --green-light: #6cb14a;
    --green-mid: #4f9f43;
    --green-dark: #3a8a3f;
    --navy: #1d4566;
    --navy-deep: #12324d;
    --black: #000000;
    --white: #ffffff;
    --orange: #e0522a;
    --logo-green: #3f9a44;
  }
  html, body {
    margin: 0;
    padding: 0;
    width: 1200px;
    height: 378px;
    overflow: hidden;
    background: var(--black);
  }
  .billboard {
    position: relative;
    width: 1200px;
    height: 378px;
    overflow: hidden;
    font-family: "Figtree", sans-serif;
  }
  .hero {
    position: absolute;
    left: 0; top: 0;
    width: 1200px;
    height: 257px;
    background: radial-gradient(ellipse at 55% 20%, var(--green-light) 0%, var(--green-mid) 55%, var(--green-dark) 100%);
    overflow: hidden;
  }
  .portrait {
    position: absolute;
    left: -287px;
    top: -81px;
    width: 574px;
    height: 574px;
    border-radius: 50%;
    background: radial-gradient(circle at 62% 45%, var(--navy) 0%, var(--navy-deep) 100%);
  }
  .location {
    position: absolute;
    right: 26px;
    top: 14px;
    display: flex;
    align-items: center;
    gap: 8px;
    color: var(--white);
    font-size: 30px;
    font-weight: 500;
    letter-spacing: 0.5px;
  }
  .location svg { width: 24px; height: 34px; }
  .headline {
    position: absolute;
    left: 315px;
    width: 800px;
    top: 56px;
    margin: 0;
    text-align: center;
    color: var(--white);
    font-size: 88px;
    font-weight: 800;
    line-height: 74px;
    letter-spacing: 0;
    white-space: nowrap;
  }
  .availability {
    position: absolute;
    left: 315px;
    width: 800px;
    top: 212px;
    margin: 0;
    text-align: center;
    color: var(--black);
    font-size: 33px;
    font-weight: 500;
    line-height: 33px;
    letter-spacing: 0.3px;
    white-space: nowrap;
  }
  .contact-bar {
    position: absolute;
    left: 0; top: 257px;
    width: 1200px;
    height: 121px;
    background: var(--black);
  }
  .brand {
    position: absolute;
    left: 24px;
    top: 0;
    height: 121px;
    display: flex;
    align-items: center;
    gap: 10px;
    color: var(--logo-green);
    font-size: 27px;
    font-weight: 800;
  }
  .brand-dot {
    width: 14px; height: 14px;
    border-radius: 50%;
    background: var(--logo-green);
  }
  .divider {
    position: absolute;
    left: 330px;
    top: 26px;
    width: 2px;
    height: 78px;
    background: var(--orange);
  }
  .phone {
    position: absolute;
    left: 362px;
    top: 10px;
    margin: 0;
    color: var(--orange);
    font-size: 86px;
    font-weight: 800;
    letter-spacing: 0.5px;
    line-height: 100px;
    white-space: nowrap;
  }
  .language {
    position: absolute;
    left: 1019px;
    top: 22px;
    margin: 0;
    color: var(--orange);
    font-size: 29px;
    font-weight: 400;
    line-height: 34px;
    text-align: center;
  }
</style>
</head>
<body>
<main class="billboard">
  <section class="hero">
    <div class="portrait" role="img" aria-label="Portrait photo of the smiling chiropractor on a navy backdrop"></div>
    <div class="location">
      <svg viewBox="0 0 24 34" aria-hidden="true">
        <path d="M12 0C5.4 0 0 5.3 0 11.8 0 20.6 12 34 12 34s12-13.4 12-22.2C24 5.3 18.6 0 12 0zm0 17a5.3 5.3 0 1 1 0-10.6A5.3 5.3 0 0 1 12 17z" fill="#ffffff"/>
      </svg>
      <span>ACROSS GEORGIA</span>
    </div>
    <h1 class="headline">INJURED IN A<br>CAR ACCIDENT?</h1>
    <p class="availability">SAME DAY APPOINTMENTS</p>
  </section>
  <section class="contact-bar">
    <div class="brand">
      <span class="brand-dot"></span>
      <span class="brand-name">Kestrelwood Rehab</span>
    </div>
    <div class="divider"></div>
    <p class="phone">(770) 48-SPINE</p>
    <p class="language">HABLA<br>ESPANOL</p>
  </section>
</main>
</body>
</html>
```